make a fireworks website

we are manufacturer of fireworks in Asia.
we need a HD fireworks website for showing product to all world customers.
we also need an register for member system,location, forum,products..etc
I added my Logo for the company.
brightnova.com.hk

and please message me if you have
any question.
here some example of website:
http://www.skyplumeshow.com/
http://www.tornelupyro.com/
http://www.quarvel-pyro.co.uk/
http://www.mirethpyro.co.uk/

```html
<!DOCTYPE html>
<html lang="en">
<head>
<meta charset="utf-8">
<title>Brightnova – Fireworks Manufacturer</title>
<link href="https://fonts.googleapis.com/css2?family=Roboto:ital,wght@0,400;0,500;0,700;1,500&family=Roboto+Condensed:wght@700&display=swap" rel="stylesheet">
<style>
:root{
  --yellow:#f6e10a;
  --yellow-deep:#f2c400;
  --purple:#5b2a86;
  --purple-dark:#3d1763;
  --magenta:#d81b7a;
  --blue:#1f6fb5;
  --red:#c8102e;
  --grey-panel:#8d8d8d;
  --page:#ecebef;
  --text:#555;
  --white:#fff;
  --button:#f5c400;
}
*{box-sizing:border-box;margin:0;padding:0}
html,body{width:711px;height:1200px;overflow:hidden}
body{background:var(--page);font-family:"Roboto",sans-serif;color:var(--text);font-size:7px;line-height:1.45;position:relative}

.site-header{position:absolute;left:0;top:0;width:711px;height:96px;
  background:linear-gradient(90deg,var(--yellow) 0,var(--yellow-deep) 55%,#2a1237 70%,#11071d 100%)}
.header-photo{position:absolute;right:0;top:0;width:260px;height:96px;
  background:radial-gradient(circle at 60% 40%,#e86a2a 0,#7a2a6a 30%,#1a0a24 70%)}
.utility-links{position:absolute;left:400px;top:0;height:16px;width:221px;background:var(--purple);
  display:flex;justify-content:space-around;align-items:center;color:var(--white);font-size:6.5px}
.brand{position:absolute;left:92px;top:24px;font-family:"Roboto Condensed",sans-serif;font-weight:700;font-size:30px;color:var(--red);display:flex;align-items:center;gap:7px}
.brand-dot{width:14px;height:14px;border-radius:50%;background:var(--red)}
.account-buttons{position:absolute;left:480px;top:40px;display:flex;gap:8px}
.account-buttons span{background:var(--white);color:var(--purple);font-size:7px;padding:2px 9px;border-radius:2px;display:flex;align-items:center;gap:3px}
.main-nav{position:absolute;left:266px;top:66px;width:355px;height:22px;background:var(--purple);display:flex;align-items:center;padding:0 4px;gap:4px;color:var(--white);font-size:7.5px}
.main-nav a{color:inherit;text-decoration:none;padding:3px 10px;border-radius:2px}
.main-nav a.active{background:var(--white);color:var(--purple)}

.info-bar{position:absolute;left:90px;top:100px;width:531px;height:24px;background:var(--white);display:flex;align-items:center;padding:0 8px;gap:18px;font-size:7px}
.info-bar .item{display:flex;align-items:center;gap:4px}
.search{margin-left:auto;display:flex}
.search span{width:130px;height:14px;border:1px solid #ccc;font-size:6.5px;color:#999;padding:1px 5px}
.search i{width:18px;height:14px;background:var(--magenta);display:block}

.hero{position:absolute;left:0;top:130px;width:711px;height:202px;
  background:radial-gradient(circle at 20% 35%,#f0a04a 0,#b0426f 18%,transparent 40%),
  radial-gradient(circle at 80% 30%,#f7d66a 0,#c05030 15%,transparent 38%),
  linear-gradient(180deg,#2a1034 0,#4a1c4a 60%,#6b2a44 100%)}
.hero-title{position:absolute;left:0;width:711px;top:60px;text-align:center;color:var(--white);font-weight:700;text-shadow:0 1px 3px rgba(0,0,0,.5)}
.hero-title .small{display:block;font-size:21px;padding-left:40px}
.hero-title .big{display:block;font-size:32px;line-height:1.1}

.content{position:absolute;left:90px;top:332px;width:531px;height:534px;background:var(--white);padding:14px 12px}
.col-left{position:absolute;left:12px;top:14px;width:245px}
.col-right{position:absolute;left:270px;top:14px;width:250px}
h2{color:var(--blue);font-size:12px;font-weight:500;margin-bottom:5px}
.section p{margin-bottom:5px}
.section{margin-bottom:14px}
.btn{display:inline-block;background:var(--button);color:#333;font-size:6.5px;padding:2px 9px;border-radius:1px}
.btn-row{display:flex;justify-content:flex-end;gap:6px;margin-top:4px}
.btn.ghost{background:#eee;border:1px solid #ccc}

.products{background:var(--grey-panel);padding:8px;height:302px}
.products-head{display:flex;justify-content:space-between;align-items:center;background:#eee;padding:3px 6px;margin:-8px -8px 8px;height:20px}
.products-head h3{font-size:11px;color:#333;font-weight:700}
.arrows{display:flex;gap:3px}
.arrows i{width:10px;height:10px;background:#ccc;display:block}
.product-grid{display:grid;grid-template-columns:1fr 1fr;gap:8px 10px}
.product-card{text-align:center;color:var(--white);font-size:6.5px}
.product-photo{height:68px;border:2px solid var(--white);margin-bottom:2px}
.quality{margin-top:14px}

.testimonial{position:absolute;left:90px;top:866px;width:531px;height:98px;background:var(--white);border-top:1px solid #ddd;text-align:center;padding:10px 40px}
.testimonial h2{color:var(--purple);font-size:11px}
.testimonial .name{color:var(--magenta);font-size:8px;font-weight:500;margin-top:4px}

.site-footer{position:absolute;left:0;top:972px;width:711px;height:228px;background:linear-gradient(180deg,var(--purple) 0,var(--purple-dark) 100%);color:var(--white);text-align:center}
.signup-title{font-size:12px;font-weight:500;font-style:italic;color:var(--yellow);text-transform:uppercase;margin-top:16px}
.signup-form{display:flex;justify-content:center;margin-top:10px}
.signup-form span{width:200px;height:16px;background:#7d52a4;font-size:6.5px;text-align:left;padding:2px 6px;color:#ddd}
.signup-form b{background:var(--purple-dark);font-size:7px;padding:2px 10px;font-weight:500}
.footer-links{display:flex;justify-content:center;gap:14px;margin-top:20px;font-size:7px}
.copyright{font-size:6.5px;margin-top:6px}
.footer-brand{font-family:"Roboto Condensed",sans-serif;font-weight:700;font-size:18px;color:var(--yellow);margin-top:20px}
.payments{display:flex;justify-content:center;gap:5px;margin-top:14px}
.payments i{width:20px;height:12px;background:#ddd;border-radius:1px;display:block}
</style>
</head>
<body>
<header class="site-header">
  <div class="header-photo" role="img" aria-label="Fireworks bursting in the night sky"></div>
  <nav class="utility-links"><span>About</span><span>Video</span><span>Gallery</span><span>Delivery</span><span>Your Account</span></nav>
  <div class="brand"><span class="brand-dot"></span>Brightnova</div>
  <div class="account-buttons">
    <span><svg width="6" height="8" viewBox="0 0 6 8"><path d="M3 0a3 3 0 0 0-3 3c0 2 3 5 3 5s3-3 3-5a3 3 0 0 0-3-3z" fill="#5b2a86"/></svg>Location</span>
    <span>Sign Up</span>
  </div>
  <nav class="main-nav"><a class="active">Home</a><a>Products ▾</a><a>Event Displays ▾</a><a>Special Offers</a><a>Contact Us</a></nav>
</header>

<div class="info-bar">
  <div class="item"><svg width="9" height="7" viewBox="0 0 9 7"><rect width="9" height="7" fill="#d81b7a"/><path d="M0 0l4.5 4L9 0" stroke="#fff" fill="none"/></svg>info@brightnova.com.hk</div>
  <div class="item"><svg width="7" height="8" viewBox="0 0 7 8"><rect x="1" width="5" height="8" rx="1" fill="#d81b7a"/></svg>+852-300-4120-7781</div>
  <div class="search"><span>Find Your Buy Words</span><i></i></div>
</div>

<section class="hero" role="img" aria-label="Colourful fireworks display over a city at night">
  <div class="hero-title"><span class="small">On Special Days,</span><span class="big">Special Fireworks</span></div>
</section>

<main class="content">
  <div class="col-left">
    <section class="section">
      <h2>Fireworks</h2>
      <p>We craft bright aerial shells, cakes and rockets in our own plant, test every batch by hand and ship certified stock to clubs, towns and families around the world.</p>
      <p>Our team has spent two decades refining colour, timing and noise so that each show lands right.</p>
      <div class="btn-row"><span class="btn ghost">Customer Login</span><span class="btn">Start Shopping</span></div>
    </section>
    <section class="section">
      <h2>Fireworks for Sale Online</h2>
      <p>Browse the full range online, pick your items by size or effect and order in a few steps. Members see trade prices and can track every order from our warehouse.</p>
      <p>New lines arrive each season, from quiet garden packs to large display batteries.</p>
      <p>Ask our staff for advice on safe distances and local rules.</p>
      <div class="btn-row"><span class="btn">Start Shopping</span></div>
    </section>
    <section class="section">
      <h2>Delivery and Collections</h2>
      <p>We deliver by licensed carrier to most regions, or you may collect from our depot by appointment.</p>
      <p>Sea freight for trade buyers leaves weekly with full paperwork.</p>
      <div class="btn-row"><span class="btn">Read More</span></div>
    </section>
  </div>

  <div class="col-right">
    <section class="products">
      <div class="products-head"><h3>Products</h3><div class="arrows"><i></i><i></i></div></div>
      <div class="product-grid">
        <div class="product-card"><div class="product-photo" role="img" aria-label="Single ignition barrage box" style="background:linear-gradient(135deg,#c84a2a,#6a2a5a)"></div>Single Ignition Barrages</div>
        <div class="product-card"><div class="product-photo" role="img" aria-label="Catherine wheel firework" style="background:radial-gradient(circle,#f0d040,#2a7ac0 60%,#1a2a60)"></div>Catherine Wheels</div>
        <div class="product-card"><div class="product-photo" role="img" aria-label="Cat 4 cake battery box" style="background:linear-gradient(135deg,#b08040,#503020)"></div>Cat 4 Cake Batteries</div>
        <div class="product-card"><div class="product-photo" role="img" aria-label="Cat 4 one box battery" style="background:linear-gradient(135deg,#d0a060,#704020)"></div>Cat 4 One Box Batteries</div>
        <div class="product-card"><div class="product-photo" role="img" aria-label="Gold fireworks pack" style="background:linear-gradient(135deg,#e0c060,#8a6a20)"></div>Gold Fireworks</div>
        <div class="product-card"><div class="product-photo" role="img" aria-label="Bundle of rockets" style="background:linear-gradient(135deg,#e0e0e0,#8080a0)"></div>Rockets</div>
      </div>
    </section>
    <section class="section quality">
      <h2>Quality Brands</h2>
      <p>Every item we sell passes strict checks for burn time, lift and fallout before it leaves the line.</p>
      <p>We work with trusted partners to bring you tested brands at fair prices.</p>
    </section>
  </div>
</main>

<section class="testimonial">
  <h2>What Say's Our Client's</h2>
  <p>The show for our city festival was flawless and the team helped us plan every cue. Delivery came early and the crowd loved it.</p>
  <div class="name">Lena Corvath</div>
  <div>Events Lead</div>
</section>

<footer class="site-footer">
  <div class="signup-title">Sign up for all of our latest offers &amp; special deals</div>
  <div class="signup-form"><span>Enter Your Email</span><b>Submit</b></div>
  <nav class="footer-links"><span>Home</span><span>|</span><span>Products</span><span>|</span><span>Event Displays</span><span>|</span><span>Special Offers</span><span>|</span><span>Contact Us</span><span>|</span><span>Location</span></nav>
  <div class="copyright">Copyright © 2014 brightnova.com.hk All Rights Reserved</div>
  <div class="footer-brand">Brightnova</div>
  <div class="payments"><i></i><i></i><i></i><i></i><i></i><i></i><i></i></div>
</footer>
</body>
</html>
```